Flyer Design

We are and electrical contractor based in Sydney. The company is called QRD Electric. We have been in business for 10 years and predominately work for construction companies. I would like the design to replicate our web site (www.qrdelectric.com) and demonstrate our ability to undertake small, medium and large building refurbishments and construction work.

Target Market(s)

NSW based building contractors and project managers. Males aged between 30 to 50 with tertiary education. We will be targeting the middle to upper management including the internal project amendment teams and estimators.

Industry/Entity Type

Construction

Font styles to use
Sans Serif

Colors

Designer to choose colors to be used in the design.

Requirements
Must have
• A detailed description of our capabilities and experience as detailed on our website. Included projects and images of these projects. Flyer must be in keeping with the colours and themes on the website.

```html
<!DOCTYPE html>
<html lang="en">
<head>
<meta charset="utf-8">
<title>QRD Electric – Flyer</title>
<link rel="stylesheet" href="https://fonts.googleapis.com/css2?family=Cabin:wght@400;500&display=swap">
<style>
  :root {
    --stage: #16263d;
    --page-black: #0b0c0f;
    --panel: rgba(12, 13, 17, 0.86);
    --ink-light: #e6e8ec;
    --ink-soft: #c9ccd2;
    --accent-blue: #3fa6e8;
    --sky-deep: #3b6fa8;
    --sky-light: #a9cdea;
    --stone: #cfc6b4;
    --steel: #8aa2b8;
  }
  * { margin: 0; padding: 0; box-sizing: border-box; }
  html, body { width: 848px; height: 1200px; overflow: hidden; }
  body {
    background: var(--stage);
    font-family: "Cabin", sans-serif;
    position: relative;
  }
  .flyer-page {
    position: absolute;
    top: 322px;
    width: 392px;
    height: 555px;
    background: var(--page-black);
    overflow: hidden;
    box-shadow: 0 6px 18px rgba(0,0,0,0.45);
  }
  .flyer-front { left: 24px; }
  .flyer-back { left: 432px; }
  .page-art { position: absolute; inset: 0; width: 100%; height: 100%; }
  .brand-name {
    position: absolute;
    display: flex;
    align-items: center;
    gap: 8px;
    color: var(--ink-light);
    font-weight: 500;
    white-space: nowrap;
  }
  .brand-mark {
    width: 10px; height: 10px;
    background: var(--accent-blue);
  }
  .flyer-front .brand-name {
    top: 112px; left: 0; right: 0;
    justify-content: center;
    font-size: 26px;
    letter-spacing: 1px;
  }
  .about-panel {
    position: absolute;
    left: 0; top: 186px;
    width: 300px; height: 266px;
    background: var(--panel);
    padding: 16px 14px 14px 16px;
    color: var(--ink-soft);
    font-size: 8.2px;
    line-height: 1.3;
  }
  .about-panel p + p { margin-top: 10px; }
  .back-footer {
    position: absolute;
    left: 0; right: 0; bottom: 0;
    height: 92px;
    background: var(--page-black);
  }
  .flyer-back .brand-name {
    left: 30px; top: 34px;
    font-size: 17px;
  }
  .tagline {
    position: absolute;
    right: 26px; top: 40px;
    color: var(--ink-light);
    font-size: 11px;
    letter-spacing: 0.6px;
  }
</style>
</head>
<body>

<section class="flyer-page flyer-front">
  <svg class="page-art" viewBox="0 0 392 555" aria-hidden="false">
    <defs>
      <linearGradient id="front-photo-a" x1="0" y1="0" x2="0" y2="1">
        <stop offset="0" stop-color="#6f9fd2"/>
        <stop offset="0.55" stop-color="#c8d4dc"/>
        <stop offset="1" stop-color="#6c6a58"/>
      </linearGradient>
      <linearGradient id="front-photo-b" x1="1" y1="0" x2="0" y2="1">
        <stop offset="0" stop-color="#5a8cc4"/>
        <stop offset="0.6" stop-color="#8fa3ad"/>
        <stop offset="1" stop-color="#c7c0ac"/>
      </linearGradient>
    </defs>
    <polygon points="0,170 212,555 0,555" fill="url(#front-photo-a)" role="img" aria-label="Photo of a completed multi-storey residential building at dusk"/>
    <line x1="0" y1="170" x2="212" y2="555" stroke="var(--accent-blue)" stroke-width="2.5"/>
    <polygon points="392,282 392,330 262,555 100,555" fill="url(#front-photo-b)" role="img" aria-label="Photo of a commercial building entrance with project signage"/>
    <line x1="392" y1="282" x2="100" y2="555" stroke="var(--accent-blue)" stroke-width="2.5"/>
  </svg>
  <div class="brand-name"><span class="brand-mark"></span>QRD Electric</div>
</section>

<section class="flyer-page flyer-back">
  <svg class="page-art" viewBox="0 0 392 555">
    <defs>
      <linearGradient id="back-photo-canopy" x1="0" y1="0" x2="0" y2="1">
        <stop offset="0" stop-color="#2f5f96"/>
        <stop offset="1" stop-color="#dfe7ee"/>
      </linearGradient>
      <linearGradient id="back-photo-glass" x1="0" y1="0" x2="1" y2="1">
        <stop offset="0" stop-color="#9cc3e2"/>
        <stop offset="1" stop-color="#5f7f98"/>
      </linearGradient>
      <linearGradient id="back-photo-plaza" x1="0" y1="0" x2="0" y2="1">
        <stop offset="0" stop-color="#b9c6cf"/>
        <stop offset="1" stop-color="#4a5158"/>
      </linearGradient>
    </defs>
    <rect x="0" y="0" width="392" height="463" fill="url(#back-photo-plaza)" role="img" aria-label="Photo of a stadium forecourt with lit bollards"/>
    <polygon points="0,0 230,0 170,190 0,190" fill="url(#back-photo-canopy)" role="img" aria-label="Photo of a tensile shade canopy at night"/>
    <polygon points="230,0 292,0 258,60 205,80" fill="#6a5a44" role="img" aria-label="Photo of a timber venue signage wall"/>
    <polygon points="292,0 392,0 392,330 300,330 258,60" fill="url(#back-photo-glass)" role="img" aria-label="Photo of a glazed commercial building facade"/>
    <polygon points="0,120 392,70 392,110 0,200" fill="#d9e3ea" opacity="0.55"/>
    <line x1="230" y1="0" x2="170" y2="190" stroke="var(--accent-blue)" stroke-width="2"/>
    <line x1="292" y1="0" x2="258" y2="60" stroke="var(--accent-blue)" stroke-width="2"/>
    <line x1="258" y1="60" x2="392" y2="330" stroke="var(--accent-blue)" stroke-width="2"/>
  </svg>
  <div class="about-panel">
    <p>QRD Electric's team of dynamic and committed employees have successfully accomplished and completed an ever-expanding portfolio. This has been possible through the collaboration of over 50 years of combined expertise in the electrical industry.</p>
    <p>Over the years we have been able to successfully manage and deliver residential, commercial and industrial projects to the highest of standards but not without the challenges that the industry presents. However we pride our selves in the way we approach these challenges with a willingness to succeed.</p>
    <p>To assist with these challenges we have implemented robust management systems and periodically revise our procedures to ensure that we operate effectively as a company, translating our hard work into competitive, results-driven outcomes.</p>
  </div>
  <footer class="back-footer">
    <div class="brand-name"><span class="brand-mark"></span>QRD Electric</div>
    <div class="tagline">PURSUIT OF EXELLENCE</div>
  </footer>
</section>

</body>
</html>
```